oloperra Web Design Project

It is a virtual assistance/concierge company that helps the busy professional by remotely providing administrative, technical and/or creative business support services, specializing in the medical device industry. Company name is oloperra.
(website will be oloperra.example)

Allowing things to be done without taking time away from more urgent issues or family/personal time. Partnering with a VA reduces stress, protects cash flow, eliminates administrative hassles, and enables business people to find the success they originally set out to achieve. Saves small businesses and/or individuals on overhead, salary, et. Work is done remotely to offer administrative, clerical, typing and specialist service assistance on a regular, ad-hoc or emergency cover basis.

Though we are capable of addressing the needs of medical professionals and industry representatives due to our experience and knowledge (sales, HCC guidelines, etc.) we do not want to be limited to that market only.

Target Market(s)

Target market would be M/F, 30-50, National, busy, Alpha, entrepreneurs and industry professionals who want/need to do more without sacrifice of life

Industry/Entity Type

Industry

Requirements
Nice to have
• We do have a logo designed via the MakerFolk website that can/should be included. Logo is uploaded.

```html
<!DOCTYPE html>
<html lang="en">
<head>
<meta charset="utf-8">
<title>oloperra — Virtual Assistance</title>
<link rel="stylesheet" href="https://fonts.googleapis.com/css2?family=Gelasio:ital,wght@0,400;1,400;1,700&family=Noto+Sans:wght@400;700&family=Arimo:ital,wght@0,400;0,700;1,700&display=swap">
<style>
:root{
  --ink:#333333;
  --muted:#666666;
  --soft:#888888;
  --line:#cfcfcf;
  --blue:#1f74bb;
  --navy:#1c2f5e;
  --red:#cc1f2a;
  --page:#ffffff;
  --footer:#f6f6f6;
  --dot:#8c8c8c;
}
*{box-sizing:border-box;margin:0;padding:0}
html,body{width:722px;height:1200px;overflow:hidden;background:var(--page)}
body{position:relative;font-family:"Noto Sans",Verdana,sans-serif;color:var(--ink)}
.abs{position:absolute}

/* header */
.brand{left:73px;top:30px;display:flex;align-items:center;gap:8px}
.brand-mark{width:14px;height:14px;border-radius:50%;background:var(--red)}
.brand-name{font-family:"Arimo",Arial,sans-serif;font-size:34px;color:var(--navy);letter-spacing:-0.5px;line-height:1}
.callout{right:70px;top:27px;font-family:"Arimo",Arial,sans-serif;font-size:12px;color:var(--muted)}
.search{left:518px;top:52px;width:134px;height:23px;border:1px solid #c5c5c5;border-radius:3px;font-size:11px;color:var(--muted);padding:4px 7px;font-family:"Arimo",Arial,sans-serif}
.search svg{position:absolute;right:7px;top:5px}

/* navigation */
.nav{left:72px;top:93px;width:581px;height:47px;border:1px solid var(--line);border-radius:5px;box-shadow:0 1px 2px rgba(0,0,0,.12)}
.nav span{position:absolute;top:16px;font-size:13px;color:#444}
.nav .active{text-decoration:underline}

/* hero */
.hero{left:73px;top:152px;width:580px;height:242px;box-shadow:0 1px 4px rgba(0,0,0,.35);
  background:linear-gradient(90deg,#e9e4df 0%,#d9c2b2 25%,#e9d6c8 50%,#d8b8a3 75%,#efe6de 100%)}
.dots{left:346px;top:406px;display:flex;gap:4px}
.dots i{width:7px;height:7px;border-radius:50%;background:var(--dot)}
.dots i:first-child{background:var(--blue)}

/* feature columns */
.feature{top:451px;width:180px}
.feature h3{font-family:"Gelasio",Georgia,serif;font-style:italic;font-weight:700;font-size:13px;text-align:center;color:#222;height:32px}
.feature .photo{height:104px;border:1px solid #bdbdbd;box-shadow:0 1px 3px rgba(0,0,0,.2)}
.feature p{margin-top:18px;font-size:12px;line-height:16px;color:#444;padding-left:1px}
.btn{display:block;width:51px;height:26px;border:1px solid #c9c9c9;border-radius:4px;font-size:11px;color:var(--blue);text-align:center;line-height:24px;box-shadow:1px 1px 2px rgba(0,0,0,.18);background:#fff}
.feature .btn{margin-top:12px;margin-left:1px}

/* welcome + services */
.section-title{font-family:"Gelasio",Georgia,serif;font-style:italic;font-size:14px;color:#333}
.section-title b{color:var(--blue);font-weight:700}
.welcome{left:75px;top:737px;width:375px}
.welcome p{margin-top:10px;font-size:12px;line-height:20px;color:#444}
.welcome .btn{position:absolute;top:180px;left:0}
.services{left:465px;top:737px;width:180px}
.services ul{list-style:none;margin-top:9px}
.services li{display:flex;align-items:center;gap:10px;font-size:11.5px;color:#444;height:24.4px}
.services .btn{position:absolute;top:180px;left:-1px}

/* clients */
.clients{left:73px;top:959px;width:580px;height:155px;border:1px solid var(--line);border-radius:4px;box-shadow:0 1px 4px rgba(0,0,0,.18)}
.clients .section-title{position:absolute;left:12px;top:8px}
.clients .rule{position:absolute;left:11px;right:14px;top:30px;border-top:1px solid #d6d6d6}
.clients .arrows{position:absolute;right:17px;top:8px;display:flex;gap:4px}
.client{position:absolute;top:42px;width:125px}
.client .photo{height:74px;border:1px solid #bdbdbd;background:linear-gradient(135deg,#b9aa97,#dcc3ad 55%,#8a9388)}
.client span{display:block;margin-top:11px;font-family:"Gelasio",Georgia,serif;font-style:italic;font-size:10.5px;color:#333;padding-left:3px}

/* footer */
.footer{left:0;top:1133px;width:722px;height:67px;background:var(--footer);border-top:1px solid #dcdcdc}
.footer-info{left:77px;top:1141px;font-family:"Arimo",Arial,sans-serif;font-size:9px;line-height:11px;color:var(--soft)}
.footer-info strong{display:block;font-size:12px;line-height:15px;font-style:italic;text-decoration:underline;color:#777}
.social{left:529px;top:1152px;display:flex;align-items:center;gap:6px;font-family:"Arimo",Arial,sans-serif;font-size:9px;color:var(--muted)}
.social i{width:13px;height:13px;border-radius:2px}
.copyright{right:77px;top:1172px;font-family:"Arimo",Arial,sans-serif;font-size:9px;color:var(--muted)}
</style>
</head>
<body>

<header>
  <div class="abs brand"><span class="brand-mark"></span><span class="brand-name">oloperra</span></div>
  <div class="abs callout">Call us @ 1800 - 55 - 730418</div>
  <div class="abs search">search...
    <svg width="12" height="12" viewBox="0 0 12 12"><circle cx="5" cy="5" r="3.6" fill="none" stroke="#8a8a8a" stroke-width="1.5"/><line x1="7.6" y1="7.6" x2="11" y2="11" stroke="#8a8a8a" stroke-width="2"/></svg>
  </div>
  <nav class="abs nav">
    <span class="active" style="left:30px">Home</span>
    <span style="left:110px">|</span>
    <span style="left:158px">About Us</span>
    <span style="left:262px">|</span>
    <span style="left:310px">Our Services</span>
    <span style="left:438px">|</span>
    <span style="left:481px">Contact Us</span>
  </nav>
</header>

<div class="abs hero" role="img" aria-label="Photo of three smiling call-centre agents wearing headsets"></div>
<div class="abs dots"><i></i><i></i><i></i><i></i></div>

<section class="abs feature" style="left:74px">
  <h3>Recieving calls</h3>
  <div class="photo" role="img" aria-label="Photo of a smiling agent with a headset in an office" style="background:linear-gradient(90deg,#8f7a52,#c9a77d 55%,#e8e0d2)"></div>
  <p>Put here something about collection of client query or calls to researching over them in a brief.</p>
  <span class="btn">More</span>
</section>
<section class="abs feature" style="left:272px">
  <h3>Reserching Issues</h3>
  <div class="photo" role="img" aria-label="Photo of a man working at desk with two monitors" style="background:linear-gradient(135deg,#6f6a5a,#a9a89c 45%,#7d8fb3)"></div>
  <p>Put here something about researching of client query or calls to researching over them in a brief.</p>
  <span class="btn">More</span>
</section>
<section class="abs feature" style="left:471px">
  <h3>Resolving Problems</h3>
  <div class="photo" role="img" aria-label="Photo of two business people shaking hands" style="background:linear-gradient(90deg,#2a3550,#b78d72 50%,#2c3854 80%,#dfe6ef)"></div>
  <p>Put here something about resolving of client query or calls to researching over them in a brief.</p>
  <span class="btn">More</span>
</section>

<section class="abs welcome">
  <h2 class="section-title"><b>Welcome</b> to our site</h2>
  <p>It is a virtual assistance/concierge company that helps the busy professional by remotely providing administrative, technical and/or creative business support services, specializing in the medical device industry. Company name is oloperra. It is a virtual assistance/concierge company that helps the busy professional by remotely providing administrative, technical and/or creative business support services.</p>
  <span class="btn">More</span>
</section>

<section class="abs services">
  <h2 class="section-title"><b>Our</b> Services</h2>
  <ul>
    <li><svg width="14" height="14" viewBox="0 0 14 14"><circle cx="7" cy="7" r="6" fill="#eef3f7" stroke="#9db4c6"/><path d="M5.5 4.3 9.5 7 5.5 9.7Z" fill="var(--blue)"/></svg>Service goes here</li>
    <li><svg width="14" height="14" viewBox="0 0 14 14"><circle cx="7" cy="7" r="6" fill="#eef3f7" stroke="#9db4c6"/><path d="M5.5 4.3 9.5 7 5.5 9.7Z" fill="var(--blue)"/></svg>Service goes here</li>
    <li><svg width="14" height="14" viewBox="0 0 14 14"><circle cx="7" cy="7" r="6" fill="#eef3f7" stroke="#9db4c6"/><path d="M5.5 4.3 9.5 7 5.5 9.7Z" fill="var(--blue)"/></svg>Service goes here</li>
    <li><svg width="14" height="14" viewBox="0 0 14 14"><circle cx="7" cy="7" r="6" fill="#eef3f7" stroke="#9db4c6"/><path d="M5.5 4.3 9.5 7 5.5 9.7Z" fill="var(--blue)"/></svg>Service goes here</li>
    <li><svg width="14" height="14" viewBox="0 0 14 14"><circle cx="7" cy="7" r="6" fill="#eef3f7" stroke="#9db4c6"/><path d="M5.5 4.3 9.5 7 5.5 9.7Z" fill="var(--blue)"/></svg>Service goes here</li>
    <li><svg width="14" height="14" viewBox="0 0 14 14"><circle cx="7" cy="7" r="6" fill="#eef3f7" stroke="#9db4c6"/><path d="M5.5 4.3 9.5 7 5.5 9.7Z" fill="var(--blue)"/></svg>Service goes here</li>
  </ul>
  <span class="btn">More</span>
</section>

<section class="abs clients">
  <h2 class="section-title"><b>Our</b> Clients</h2>
  <div class="arrows">
    <svg width="14" height="14" viewBox="0 0 14 14"><circle cx="7" cy="7" r="6" fill="#eef3f7" stroke="#9db4c6"/><path d="M8.5 4.3 4.5 7 8.5 9.7Z" fill="var(--blue)"/></svg>
    <svg width="14" height="14" viewBox="0 0 14 14"><circle cx="7" cy="7" r="6" fill="#eef3f7" stroke="#9db4c6"/><path d="M5.5 4.3 9.5 7 5.5 9.7Z" fill="var(--blue)"/></svg>
  </div>
  <div class="rule"></div>
  <figure class="client" style="left:10px"><div class="photo" role="img" aria-label="Client photo: smiling woman resting her chin on her hand"></div><span>Maplebrook Clinic</span></figure>
  <figure class="client" style="left:154px"><div class="photo" role="img" aria-label="Client photo: smiling woman resting her chin on her hand"></div><span>Maplebrook Clinic</span></figure>
  <figure class="client" style="left:298px"><div class="photo" role="img" aria-label="Client photo: smiling woman resting her chin on her hand"></div><span>Maplebrook Clinic</span></figure>
  <figure class="client" style="left:439px"><div class="photo" role="img" aria-label="Client photo: smiling woman resting her chin on her hand"></div><span>Maplebrook Clinic</span></figure>
</section>

<footer>
  <div class="abs footer"></div>
  <div class="abs footer-info">
    <strong>oloperra</strong>
    Emergency Call : 1800-00-4471<br>
    Fax : 6510093372<br>
    E-mail : help4@oloperra.example
  </div>
  <div class="abs social">Find Us :
    <i style="background:#3b5a9a" aria-label="Social profile"></i>
    <i style="background:#4aa8d8" aria-label="Social profile"></i>
    <i style="background:#1f6fa8" aria-label="Social profile"></i>
  </div>
  <div class="abs copyright">Copyright 2012 | Privacy Policy</div>
</footer>

</body>
</html>
```